Updating our Raw Materials Brochure

Please update and modify (to add more space for the additional text) the brochure designed for us in January (see attached file) so we can circulate a May 2021 version. Thanks and hope your family is OK despite the terrible tragedy going on with Covid-19 in India. Best wishes!

```html
<!DOCTYPE html>
<html lang="en">
<head>
<meta charset="utf-8">
<title>Raw Materials – May 2021 Market Update</title>
<link href="https://fonts.googleapis.com/css2?family=Montserrat:wght@300;600;700;800&family=Open+Sans:wght@400;600;700&display=swap" rel="stylesheet">
<style>
:root{
  --red:#e81d25;
  --ink:#1a1a1a;
  --text:#222;
  --white:#fff;
  --paper:#f6f6f6;
  --stage:#7d7d7d;
  --blue:#4a86d8;
  --orange:#f07f2a;
}
*{box-sizing:border-box;margin:0;padding:0}
html,body{width:1200px;height:787px;overflow:hidden;background:var(--stage)}
body{position:relative;font-family:"Open Sans",Arial,sans-serif;color:var(--text)}
.page{position:absolute;top:71px;width:498px;height:645px;background:var(--paper);overflow:hidden;box-shadow:0 4px 14px rgba(0,0,0,.35)}
.page--front{left:72px}
.page--back{left:629px}
.abs{position:absolute}

.top-rule{left:0;top:0;width:100%;height:3px;background:var(--red)}
.web-tab{right:0;top:0;width:218px;height:34px;background:var(--red);clip-path:polygon(0 0,100% 0,100% 100%,22px 100%);color:var(--white);font:600 11px/34px "Montserrat",sans-serif;letter-spacing:2px;text-align:right;padding-right:26px}
.brand{left:26px;top:44px;display:flex;align-items:center;gap:8px;font:800 21px/1 "Montserrat",sans-serif;color:var(--ink);letter-spacing:.3px}
.brand-dot{width:20px;height:20px;border-radius:50%;background:var(--red)}
.call-label{left:299px;top:46px;font:700 14px/1 "Montserrat",sans-serif;color:var(--ink)}
.phone-pill{left:270px;top:66px;width:204px;height:23px;border-radius:12px;background:var(--red);color:var(--white);font:700 14px/23px "Montserrat",sans-serif;padding-left:28px}
.phone-pill svg{position:absolute;left:0;top:0}

.hero{left:0;width:100%}
.hero--front{top:105px;height:172px;background:linear-gradient(115deg,#20242b 0%,#3c4048 35%,#7a4a1e 60%,#2b2e35 100%)}
.hero--back{top:0;height:165px;background:linear-gradient(180deg,#1d2a3d 0%,#3a4456 45%,#6e5a3a 78%,#2c2a28 100%)}
.title-bar{background:var(--ink);color:var(--white);font:800 26px/34px "Montserrat",sans-serif;padding-left:14px;letter-spacing:.3px}
.title-bar--red{background:var(--red);font-size:22px;line-height:27px}

.sec-head{background:var(--red);color:var(--white);font-family:"Montserrat",sans-serif}
.sec-head::after{content:"";position:absolute;right:0;top:0;border-top:13px solid #3a1214;border-left:13px solid transparent}
.sec-head .light{display:block;font-weight:300;font-size:20px;line-height:20px}
.sec-head .bold{display:block;font-weight:800;font-size:20px;line-height:21px}
.sub-head{background:var(--red);color:var(--white);font:700 10px/12px "Montserrat",sans-serif;text-align:center;padding-top:4px}

.copy{font-size:6.6px;line-height:9.3px;text-align:justify}
.copy p{margin-bottom:3.5px}
.copy-title{font:700 8.4px/10px "Open Sans",sans-serif;color:var(--ink)}
.chart-title{font:600 7.5px/1 "Open Sans",sans-serif;color:#555;text-align:center}
svg text{font-family:"Open Sans",sans-serif}

.foot-dark{left:0;top:625px;width:100%;height:20px;background:var(--ink)}
.foot-bar{left:24px;top:610px;width:451px;height:28px;background:var(--red);display:flex;align-items:center;justify-content:space-around;color:var(--white);font:700 10px/1 "Montserrat",sans-serif}
.foot-bar .sep{width:1px;height:16px;background:var(--white)}
.bottom-rule{left:0;bottom:0;width:100%;height:3px;background:var(--red)}
</style>
</head>
<body>

<section class="page page--front">
  <div class="abs top-rule"></div>
  <div class="abs web-tab">⊕ www.kdrcoat.com</div>
  <div class="abs brand"><span class="brand-dot"></span>KDR INDUSTRIES</div>
  <div class="abs call-label">Call us at</div>
  <div class="abs phone-pill">
    <svg width="23" height="23" viewBox="0 0 23 23"><circle cx="11.5" cy="11.5" r="11.5" fill="#1a1a1a"/><path d="M8 6.5l2 .2.8 2.6-1.3 1a6 6 0 0 0 3.3 3.3l1-1.3 2.6.8.2 2c-4.5.8-9.3-4-8.6-8.6z" fill="#fff"/></svg>
    800-555-BOND (2663)
  </div>

  <div class="abs hero hero--front" role="img" aria-label="Close-up photograph of industrial machinery gears with warm metallic light"></div>
  <div class="abs title-bar" style="left:29px;top:131px;width:267px;height:34px">RAW MATERIALS</div>
  <div class="abs title-bar title-bar--red" style="left:29px;top:165px;width:136px;height:27px">MAY 2021</div>
  <div class="abs title-bar" style="left:29px;top:192px;width:267px;height:34px">MARKET UPDATE</div>

  <div class="abs sec-head" style="left:29px;top:248px;width:207px;height:54px;padding:8px 0 0 19px"><span class="light">GLOBAL</span><span class="bold">SHORTAGES</span></div>
  <div class="abs sec-head" style="left:263px;top:248px;width:207px;height:54px;padding:8px 0 0 20px"><span class="light">KEY</span><span class="bold">CONSTRAINTS</span></div>

  <div class="abs copy" style="left:29px;top:307px;width:207px">
    <p>As the recovery builds momentum more manufacturers are trying to buy extra material to prevent running out. Nearly all inputs are affected and there seems to be no end in sight as supply is unable to keep up with demand.</p>
    <p>The situation has been complicated by a growing list of disasters. Starting with the deep freeze and blackouts wiping out energy and petrochemicals operations in February, the Suez canal back up in March then hackers bringing down the largest US pipeline this month.</p>
    <p>US GDP increased at a 10.7% annual rate or $554.2 billion in current dollars (adjusted to 6.4% for inflation) in the first quarter. Demand seems to be driven by personal income growing $2.4 trillion (up 59%) from increased government social benefits and pandemic relief programs. Expectations are it will continue as personal savings were $4.12 trillion (up 83% the fourth quarter) driving personal savings to 21%.</p>
    <p>The trailing 12-month Producer Price Index and Consumer Price Index were up 6.2% and 4.2% respectively. These should go higher as the trailing 4-months averages are 10.2% and 6.3% respectively. Our procurement team is focused on leveraging our global supply position and growing demand so we will continue to deliver you the most competitive costs available despite these conditions.</p>
  </div>

  <svg class="abs" style="left:29px;top:532px" width="207" height="106" viewBox="0 0 207 106">
    <text x="0" y="4" font-size="3.2" font-weight="700">Chart 2. 12-month percent change in CPI, all urban consumers, Apr. 2020 – Apr. 2021</text>
    <text x="0" y="8" font-size="2.6" fill="#555">Percent change</text>
    <g stroke="#ddd" stroke-width=".4">
      <line x1="6" y1="12" x2="204" y2="12"/><line x1="6" y1="27" x2="204" y2="27"/><line x1="6" y1="42" x2="204" y2="42"/><line x1="6" y1="57" x2="204" y2="57"/><line x1="6" y1="72" x2="204" y2="72"/><line x1="6" y1="87" x2="204" y2="87"/>
    </g>
    <rect x="6" y="12" width="198" height="75" fill="none" stroke="#bbb" stroke-width=".4"/>
    <g font-size="3" fill="#555"><text x="2" y="13">5</text><text x="2" y="28">4</text><text x="2" y="43">3</text><text x="2" y="58">2</text><text x="2" y="73">1</text><text x="2" y="88">0</text></g>
    <polyline fill="none" stroke="#7a7ae0" stroke-width=".8" points="16,83 30,86 45,79 60,73 75,69 90,68 105,71 120,71 135,68 150,68 165,65 180,48 193,23"/>
    <polyline fill="none" stroke="#b0384a" stroke-width=".8" points="16,67 30,70 45,70 60,65 75,64 90,64 105,65 120,66 135,67 150,68 165,70 180,64 193,38"/>
    <g font-size="2.8" fill="#555"><text x="12" y="93">Apr'20</text><text x="27" y="93">May</text><text x="42" y="93">Jun</text><text x="57" y="93">Jul</text><text x="72" y="93">Aug</text><text x="87" y="93">Sep</text><text x="102" y="93">Oct</text><text x="117" y="93">Nov</text><text x="132" y="93">Dec</text><text x="147" y="93">Jan</text><text x="162" y="93">Feb</text><text x="177" y="93">Mar</text><text x="189" y="93">Apr'21</text></g>
    <line x1="45" y1="100" x2="58" y2="100" stroke="#7a7ae0" stroke-width=".8"/><text x="62" y="101" font-size="2.8">All items</text>
    <line x1="105" y1="100" x2="118" y2="100" stroke="#b0384a" stroke-width=".8"/><text x="122" y="101" font-size="2.8">All items less food and energy</text>
  </svg>

  <div class="abs copy-title" style="left:263px;top:305px">Ethylene Shortage Drives Prices Higher</div>
  <div class="abs copy" style="left:263px;top:320px;width:207px">
    <p>Contractual prices for Ethylene (key feedstock for water based and hot melt adhesives) increased 56% from 2020 to a 7-year high of $0.47/lb in March as multiple severe weather cracker outages driven by the deep freeze in February forced 70% capacity offline. Restarting production has been difficult as so many sites were damaged simultaneously.</p>
  </div>

  <div class="abs chart-title" style="left:263px;top:386px;width:207px">Ethylene, Contract and Spot Pricing</div>
  <svg class="abs" style="left:263px;top:397px" width="207" height="118" viewBox="0 0 207 118">
    <g stroke="#eee" stroke-width=".4">
      <line x1="30" y1="8" x2="200" y2="8"/><line x1="30" y1="28" x2="200" y2="28"/><line x1="30" y1="48" x2="200" y2="48"/><line x1="30" y1="68" x2="200" y2="68"/><line x1="30" y1="88" x2="200" y2="88"/><line x1="30" y1="98" x2="200" y2="98"/>
    </g>
    <g font-size="4.2" fill="#666" text-anchor="end">
      <text x="28" y="10">$0.650</text><text x="28" y="30">$0.550</text><text x="28" y="50">$0.450</text><text x="28" y="70">$0.350</text><text x="28" y="90">$0.150</text><text x="28" y="100">$0.000</text>
    </g>
    <polyline fill="none" stroke="var(--blue)" stroke-width="1" points="48,50 74,52 100,48 126,39 152,39 178,26"/>
    <polyline fill="none" stroke="var(--orange)" stroke-width="1" points="48,59 74,63 100,56 126,38 152,38 178,14"/>
    <g font-size="4.2" fill="#666" text-anchor="middle"><text x="48" y="108">Oct-20</text><text x="74" y="108">Nov-20</text><text x="100" y="108">Dec-20</text><text x="126" y="108">Jan-21</text><text x="152" y="108">Feb-21</text><text x="178" y="108">Mar-21</text></g>
    <line x1="24" y1="116" x2="36" y2="116" stroke="var(--blue)"/><text x="38" y="117.5" font-size="3.8" fill="#555">PETRODEX Contract NA Ethylene</text>
    <line x1="124" y1="116" x2="136" y2="116" stroke="var(--orange)"/><text x="138" y="117.5" font-size="3.8" fill="#555">PETRODEX Spot C2</text>
  </svg>

  <div class="abs sub-head" style="left:263px;top:521px;width:207px;height:32px">Vinyl Acetate Monomer (VAM) – Key<br>Ingredient for Water Based Adhesives</div>
  <div class="abs copy" style="left:263px;top:559px;width:207px">
    <p>VAM shortages became severe following the February winter storm driving prices up 128% since Jan-2021. All three US suppliers (Norvane, Halcrest and Brightmoor Chem) declared force majeure and all four production sites were shut down. They were stuck in varying stages of restarting and ramping up to full rates for nearly 3 months so supplies remain limited and that is expected to continue through Q2 with demand currently outstripping supply.</p>
  </div>
  <div class="abs bottom-rule"></div>
</section>

<section class="page page--back">
  <div class="abs hero hero--back" role="img" aria-label="Photograph of an oil refinery at dusk with lit towers and pipework"></div>
  <div class="abs title-bar" style="left:29px;top:36px;width:244px;height:32px;line-height:32px;font-size:24px">RAW MATERIALS</div>
  <div class="abs title-bar title-bar--red" style="left:29px;top:68px;width:124px;height:25px;line-height:25px;font-size:20px">MAY 2021</div>
  <div class="abs title-bar" style="left:29px;top:93px;width:244px;height:32px;line-height:32px;font-size:24px">MARKET UPDATE</div>

  <div class="abs sec-head" style="left:29px;top:152px;width:207px;height:43px;padding:8px 0 0 17px"><span class="bold" style="font-size:12.5px;line-height:15px">LOGISTICS LIMITATIONS VS.<br>DEMAND GROWTH</span></div>
  <div class="abs copy" style="left:29px;top:204px;width:207px">
    <p>The ramp up in production of consumer and industrial goods while consumers still rely more on at home delivery or pick up from stores (which require more trucks and warehousing) has driven unprecedented logistics tightness.</p>
  </div>

  <svg class="abs" style="left:29px;top:249px" width="207" height="120" viewBox="0 0 207 120">
    <rect width="207" height="120" fill="#fff"/>
    <text x="2" y="6" font-size="5.4" font-weight="700">A Logistical Nightmare</text>
    <text x="2" y="12" font-size="4.2" fill="#444">Transport, storage and inventory costs are near record highs in the U.S.</text>
    <g font-size="3.6" fill="#444"><line x1="2" y1="17" x2="6" y2="15" stroke="#111"/><text x="8" y="18">Transportation</text><line x1="44" y1="17" x2="48" y2="15" stroke="#e83aa6"/><text x="50" y="18">Warehousing</text><line x1="80" y1="17" x2="84" y2="15" stroke="#29a8e0"/><text x="86" y="18">Inventories</text></g>
    <text x="203" y="27" font-size="3.8" text-anchor="end">100 index level*</text>
    <g font-size="3.8" fill="#444"><text x="200" y="48">75</text><text x="200" y="70">50</text><text x="200" y="92">25</text></g>
    <text x="34" y="40" font-size="4">Expansion</text>
    <text x="72" y="86" font-size="4">Contraction</text>
    <line x1="12" y1="71" x2="195" y2="71" stroke="#e8b800" stroke-width=".6" stroke-dasharray="2 1.5"/>
    <polyline fill="none" stroke="#111" stroke-width=".8" points="6,34 14,38 20,46 28,50 36,54 42,58 50,66 56,73 62,70 70,72 76,74 84,65 92,72 100,70 108,63 114,68 120,62 128,58 134,86 142,70 150,56 156,46 162,38 170,42 176,42 182,38 190,34 196,32"/>
    <polyline fill="none" stroke="#e83aa6" stroke-width=".8" points="6,44 14,46 22,50 30,52 40,52 50,54 60,56 70,58 80,54 90,52 100,54 110,58 120,56 128,52 134,62 140,58 150,48 156,44 164,42 172,46 180,44 190,40 196,36"/>
    <polyline fill="none" stroke="#29a8e0" stroke-width=".8" points="6,46 14,48 22,52 30,50 40,54 50,54 60,56 70,54 80,58 90,58 100,56 110,60 120,58 128,56 134,60 140,56 150,56 158,52 166,52 174,54 182,50 190,46 196,40"/>
    <line x1="6" y1="98" x2="196" y2="98" stroke="#aaa" stroke-width=".4"/>
    <g font-size="4" fill="#444" text-anchor="middle"><text x="32" y="104">2019</text><text x="102" y="104">2020</text><text x="172" y="104">2021</text></g>
    <text x="2" y="110" font-size="3.5" fill="#444">Source: Freight Managers' Index</text>
    <text x="2" y="115" font-size="3.2" fill="#444">*The index is a diffusion index where 50 is the dividing line between expansion and contraction.</text>
  </svg>

  <div class="abs copy" style="left:29px;top:379px;width:207px">
    <p>Capacity is constrained by slowed construction in vehicles (chips and other materials shortages) as traditional channels are idled (shopping malls, etc.). Spot Van rates were up 58.1% versus April 2020 as outages cause chain reactions. Currently there is a traffic jam of 771 barges accumulated on the lower Mississippi due to a fractured bridge, so expectations are this will continue until year end.</p>
  </div>

  <div class="abs copy-title" style="left:29px;top:460px;font-size:7.5px">Transportation Prices</div>
  <svg class="abs" style="left:29px;top:452px" width="207" height="150" viewBox="0 0 250 150" preserveAspectRatio="none">
    <g fill="var(--blue)">
      <rect x="10" y="62.6" width="4.5" height="62.4"/><rect x="19.5" y="67.4" width="4.5" height="57.6"/><rect x="29" y="63.8" width="4.5" height="61.2"/><rect x="38.5" y="66" width="4.5" height="59"/><rect x="48" y="66.3" width="4.5" height="58.7"/><rect x="57.5" y="64.3" width="4.5" height="60.7"/><rect x="67" y="72.8" width="4.5" height="52.2"/><rect x="76.5" y="75.8" width="4.5" height="49.2"/><rect x="86" y="61.8" width="4.5" height="63.2"/><rect x="95.5" y="65" width="4.5" height="60"/><rect x="105" y="67.4" width="4.5" height="57.6"/><rect x="114.5" y="46.4" width="4.5" height="78.6"/><rect x="124" y="79.8" width="4.5" height="45.2"/><rect x="133.5" y="66.1" width="4.5" height="58.9"/><rect x="143" y="48.2" width="4.5" height="76.8"/><rect x="152.5" y="37.9" width="4.5" height="87.1"/><rect x="162" y="24.4" width="4.5" height="100.6"/><rect x="171.5" y="19.5" width="4.5" height="105.5"/><rect x="181" y="22.4" width="4.5" height="102.6"/><rect x="190.5" y="22" width="4.5" height="103"/><rect x="200" y="22.9" width="4.5" height="102.1"/><rect x="209.5" y="27.8" width="4.5" height="97.2"/><rect x="219" y="19.4" width="4.5" height="105.6"/><rect x="228.5" y="16.3" width="4.5" height="108.7"/><rect x="238" y="13.9" width="4.5" height="111.1"/>
    </g>
    <path d="M10 58 Q45 80 80 74 Q120 72 150 48 Q185 20 242 12" fill="none" stroke="#e81d25" stroke-width="1"/>
    <line x1="6" y1="125" x2="246" y2="125" stroke="#999" stroke-width=".5"/>
    <g font-size="3.6" fill="#444"><text x="9" y="60">52</text><text x="114" y="44">65.5</text><text x="123" y="78">37.7</text><text x="151" y="36">72.6</text><text x="161" y="22">83.8</text><text x="170" y="17">87.9</text><text x="227" y="14">90.6</text><text x="237" y="12">92.6</text></g>
    <g font-size="3.4" fill="#444"><text transform="translate(10 136) rotate(-40)">Apr-19</text><text transform="translate(57 136) rotate(-40)">Sep-19</text><text transform="translate(105 136) rotate(-40)">Feb-20</text><text transform="translate(152 136) rotate(-40)">Jul-20</text><text transform="translate(200 136) rotate(-40)">Dec-20</text><text transform="translate(238 136) rotate(-40)">Apr-21</text></g>
  </svg>

  <div class="abs" style="left:262px;top:175px;width:19px;height:116px;background:var(--red)">
    <div style="position:absolute;left:50%;top:50%;transform:translate(-50%,-50%) rotate(-90deg);white-space:nowrap;color:#fff;font:700 8px/1 'Montserrat',sans-serif">VAM Index</div>
  </div>
  <svg class="abs" style="left:283px;top:175px" width="186" height="137" viewBox="0 0 186 137">
    <rect width="186" height="137" fill="#fff"/>
    <g font-size="4.8" fill="#555" text-anchor="end">
      <text x="24" y="6">$2,300.0</text><text x="24" y="18">$2,100.0</text><text x="24" y="30">$1,900.0</text><text x="24" y="42">$1,700.0</text><text x="24" y="54">$1,500.0</text><text x="24" y="66">$1,300.0</text><text x="24" y="78">$1,100.0</text><text x="24" y="90">$900.0</text><text x="24" y="102">$700.0</text><text x="24" y="114">$500.0</text>
    </g>
    <polyline fill="none" stroke="var(--orange)" stroke-width="1.1" points="36,88 57,87 78,86 99,86 120,80 141,41 162,15"/>
    <g font-size="4.6" fill="#555" text-anchor="middle"><text x="36" y="124">Oct-20</text><text x="57" y="124">Nov-20</text><text x="78" y="124">Dec-20</text><text x="99" y="124">Jan-21</text><text x="120" y="124">Feb-21</text><text x="141" y="124">Mar-21</text><text x="162" y="124">Apr-21</text></g>
    <line x1="60" y1="133" x2="72" y2="133" stroke="var(--orange)"/><text x="74" y="134.5" font-size="4.2" fill="#555">CHEMQUOTE VAM FOB Spot Low ($/mt)</text>
  </svg>

  <div class="abs sec-head" style="left:262px;top:315px;width:207px;height:59px;padding:6px 0 0 16px"><span class="bold" style="font-size:12.5px;line-height:16px">Polyethylene and<br>Polyurethane Prices near<br>record highs</span></div>
  <div class="abs copy" style="left:262px;top:380px;width:207px">
    <p>About 42% of US oil refining capacity went offline in February (~5.5m barrels/day) but it has recovered to over 86% by last week. The shortages this created downstream continue to create spot outages of critical inputs resulting in reduced operating rates at our suppliers.</p>
    <p>For example, Polyethylene polymers (critical in hot melt adhesives) increased 39% this year plus Benzene increased 10% in April and Polyether Polyols (key feedstock for polyurethanes) are on 75% sales allocation because of limited domestic materials and difficulty bringing in imports from marine transport shortages. As a result, the price index for rubbers and plastics is up 9% since January and is still rising.</p>
  </div>

  <svg class="abs" style="left:262px;top:504px" width="207" height="96" viewBox="0 0 207 96">
    <rect width="207" height="96" fill="#eef2f8"/>
    <text x="3" y="6" font-size="4.6" font-weight="700">ECONDATA</text>
    <text x="26" y="5.6" font-size="2.6" fill="#444">Producer Price Index: rubber and plastic products</text>
    <rect x="10" y="10" width="193" height="70" fill="#fff"/>
    <rect x="162" y="10" width="41" height="70" fill="#fbf8d8"/>
    <polyline fill="none" stroke="#5b7db8" stroke-width=".7" points="12,64 22,63 32,63 40,61 48,55 54,52 60,53 68,50 76,48 84,42 92,40 100,38 108,37 116,38 124,38 132,39 140,40 150,40 160,42 168,44 174,46 180,42 186,38 192,30 198,16"/>
    <g font-size="2.4" fill="#666"><text x="16" y="86">Jul 2016</text><text x="56" y="86">Jul 2017</text><text x="96" y="86">Jul 2018</text><text x="136" y="86">Jul 2019</text><text x="176" y="86">Jul 2020</text></g>
    <rect x="10" y="88" width="193" height="3" fill="#c9d5ea"/>
    <text x="3" y="95" font-size="2.2" fill="#666">Shaded areas show recession periods. Source: National Labor Data Office</text>
  </svg>

  <div class="abs foot-dark"></div>
  <div class="abs foot-bar">
    <span>⊕ www.kdrcoat.com</span><span class="sep"></span>
    <span>✆ 800-555-BOND (2663)</span><span class="sep"></span>
    <span>✉ info@kdrcoat.com</span>
  </div>
</section>

</body>
</html>
```